Web Design for Palmwick Organic Soap Company

We need a website design for the company Velm Botanics based on the package design per attached.

The design should communicate high end, luxury organic. The site will provide facts about how the spread of disease causes deaths and can be prevented with hand washing. The site will also have a page about why we are passionate about organics and how that relates to our skin including skin facts.
Also, the site should have an e-commerce product page and shopping cart.

Target Market(s)

Educated, health conscious and socially conscious consumers who shop luxury. Target vendors include Tarrow Market and Bellquist..

Industry/Entity Type

E-Commerce

Font styles to use
Other font styles liked:
• See attached

Requirements
Must have
• Use of Ying Yang leaf Logo provided.
Based on design provided.

```html
<!DOCTYPE html>
<html lang="en">
<head>
<meta charset="utf-8">
<title>Velm Botanics – Organic Soap</title>
<link href="https://fonts.googleapis.com/css2?family=Yanone+Kaffeesatz:wght@300;400&family=Open+Sans:ital,wght@0,400;0,600;1,700&display=swap" rel="stylesheet">
<style>
  :root {
    --tan: #cdb08e;
    --brown: #5a4330;
    --brown-deep: #3d2a1b;
    --ink: #3a2a1c;
    --text: #4b4540;
    --red: #b43a24;
    --cream: #f6f1ea;
    --white: #ffffff;
  }
  * { box-sizing: border-box; margin: 0; padding: 0; }
  html, body { width: 1093px; height: 1200px; overflow: hidden; background: var(--white); }
  body { position: relative; font-family: "Open Sans", sans-serif; }
  .abs { position: absolute; }
  .cond { font-family: "Yanone Kaffeesatz", sans-serif; font-weight: 300; }

  .site-header { left: 0; top: 0; width: 1093px; height: 106px; background: var(--tan); }
  .brand { left: 143px; top: 28px; height: 65px; display: flex; align-items: center; gap: 10px; }
  .brand-mark { width: 44px; height: 65px; background: var(--red); }
  .brand-name { font-family: "Yanone Kaffeesatz", sans-serif; font-weight: 400; font-size: 30px; color: var(--ink); }

  .account-links { right: 176px; top: 23px; font-size: 15px; color: var(--ink); display: flex; gap: 9px; }
  .account-links .login { color: var(--red); }

  .main-nav { left: 498px; top: 64px; height: 26px; display: flex; align-items: center; font-size: 16px; color: var(--ink); }
  .main-nav a { color: inherit; text-decoration: none; }
  .main-nav .active { background: var(--brown); color: var(--white); width: 55px; height: 26px; display: flex; align-items: center; justify-content: center; margin-right: 12px; }
  .main-nav .item { margin-right: 25px; }

  .search { left: 762px; top: 64px; width: 157px; height: 26px; background: var(--cream); font-size: 14px; color: #6a5a4a; padding: 4px 9px; }
  .search svg { position: absolute; right: 8px; top: 5px; }

  .hero { left: 0; top: 106px; width: 1093px; height: 372px;
    background: linear-gradient(90deg, #b7b8ba 0%, #cfd0d2 35%, #c9a99d 60%, #d59a86 80%, #c9b8b2 100%); }
  .caption { left: 143px; height: 33px; background: var(--brown-deep); color: var(--white); font-size: 22px; display: flex; align-items: center; padding: 0 10px; }

  .pager { left: 491px; top: 494px; width: 99px; height: 30px; border-radius: 15px; background: var(--white); box-shadow: 0 4px 8px rgba(0,0,0,.18); display: flex; align-items: center; justify-content: center; gap: 8px; }
  .pager span { width: 12px; height: 12px; border-radius: 50%; border: 1px solid #aaa; background: #f2f2f2; }
  .pager .on { background: var(--tan); border-color: #b0916a; }

  .section-tab { left: 470px; top: 592px; width: 151px; height: 43px; background: var(--brown); color: var(--white); font-size: 20px; font-weight: 400; display: flex; align-items: center; justify-content: center; }
  .products { left: 143px; top: 635px; width: 802px; height: 214px; background: var(--tan); }
  .arrow { top: 86px; width: 34px; height: 47px; background: var(--brown); display: flex; align-items: center; justify-content: center; }
  .product { top: 34px; width: 187px; text-align: center; }
  .product-photo { width: 187px; height: 121px; border: 4px solid #ece4da; }
  .product-name { margin-top: 16px; font-size: 14.5px; color: var(--ink); }

  .why-heading { left: 0; width: 1093px; top: 903px; text-align: center; font-size: 17px; font-weight: 400; color: var(--ink); }
  .why-heading span { text-decoration: underline; text-underline-offset: 3px; }
  .why-text { left: 246px; width: 600px; top: 941px; text-align: center; font-size: 12px; line-height: 19px; color: var(--text); }
  .btn { left: 506px; top: 1026px; width: 91px; height: 32px; background: var(--brown); color: var(--white); font-style: italic; font-weight: 700; font-size: 12px; display: flex; align-items: center; justify-content: center; }

  .site-footer { left: 0; top: 1110px; width: 1093px; height: 90px; background: var(--brown-deep); border-top: 3px solid #2a1c11; text-align: center; font-size: 10.5px; color: #c9b49a; }
  .footer-nav { margin-top: 15px; }
  .footer-nav .current { color: var(--white); }
  .footer-nav i { font-style: normal; margin: 0 10px; }
  .copyright { margin-top: 6px; }
</style>
</head>
<body>
  <header class="abs site-header">
    <div class="abs brand"><div class="brand-mark"></div><span class="brand-name">Velm Botanics</span></div>
    <div class="abs account-links cond"><span class="login">Login</span><span>|</span><span>Register</span><span>|</span><span>Shopping Cart : 0</span></div>
    <nav class="abs main-nav cond">
      <a class="active" href="#">Home</a>
      <a class="item" href="#">About Us</a>
      <a class="item" href="#">Products</a>
      <a class="item" href="#">Contacts</a>
    </nav>
    <div class="abs search cond">Search here
      <svg width="16" height="16" viewBox="0 0 16 16"><circle cx="6.5" cy="6.5" r="5" fill="none" stroke="#5a6a7a" stroke-width="1.5"/><line x1="10" y1="10" x2="15" y2="15" stroke="#5a6a7a" stroke-width="2"/></svg>
    </div>
  </header>

  <section class="abs hero" role="img" aria-label="Photo of hands lathering organic soap under a running tap, with a boxed soap bar"></section>
  <div class="abs caption cond" style="top:213px;">Go for Organic Soap</div>
  <div class="abs caption cond" style="top:252px;">&amp; Keep away from disease</div>

  <div class="abs pager"><span class="on"></span><span></span><span></span><span></span></div>

  <div class="abs section-tab cond">OUR PRODUCTS</div>
  <section class="abs products">
    <div class="abs arrow" style="left:0;"><svg width="14" height="24" viewBox="0 0 14 24"><polyline points="12,2 2,12 12,22" fill="none" stroke="#fff" stroke-width="2"/></svg></div>
    <div class="abs product" style="left:77px;">
      <div class="product-photo" role="img" aria-label="Stacked lavender soap slabs" style="background:linear-gradient(160deg,#8a8592,#6f6a78);"></div>
      <div class="product-name">Lavender Soap</div>
    </div>
    <div class="abs product" style="left:313px;">
      <div class="product-photo" role="img" aria-label="Yellow lemongrass soap blocks" style="background:linear-gradient(160deg,#d6d070,#c4bd50);"></div>
      <div class="product-name">Emongrasstea Soap</div>
    </div>
    <div class="abs product" style="left:546px;">
      <div class="product-photo" role="img" aria-label="Clove soap bars with herbs and flowers" style="background:linear-gradient(160deg,#f2eee8,#d8c6a8);"></div>
      <div class="product-name">Soapclove</div>
    </div>
    <div class="abs arrow" style="left:768px;"><svg width="14" height="24" viewBox="0 0 14 24"><polyline points="2,2 12,12 2,22" fill="none" stroke="#fff" stroke-width="2"/></svg></div>
  </section>

  <h2 class="abs why-heading cond"><span>WHU YOU SHOULD USE ORGANIC SOAP</span></h2>
  <p class="abs why-text">The site will provide facts about how the spread of disease causes deaths and can be prevented with hand washing. The site will also have a page about why we are passionate about organics and<br>how that relates to our skin including skin facts.</p>
  <a class="abs btn">Know More</a>

  <footer class="abs site-footer">
    <div class="footer-nav"><span class="current">Home</span><i>|</i>About Us<i>|</i>Products<i>|</i>Contacts<i>|</i>Privacy Policy</div>
    <div class="copyright">Copyright@2014, Velm Botanics</div>
  </footer>
</body>
</html>
```